Wordpress Design Project (Bramblewick)

We need a wordpress design for an established auction and real estate company based in New Hampshire. The winning design will incorporate the colors of logo (red and blue) creatively with black or gray in a very professional and clean layout. Client mentions liking the site http://www.veltranbids.com/ as a general idea.

Industry/Entity Type

Real Estate

Requirements
Must have
• Navigation:
1) Home (lorem text)
2) Upcoming Auctions
3) Auction Results
4) Sell or Consign
5) About Us
6) Services
7) FAQ
8) Contact Us

Site will have slideshow, initial image attached.
Sidebar widgets:
- Email sign up form
- Featured Auction (like at http://www.dorvexsalehouse.com) - - - - Video Widget
- Testimonials widget

Footer will have smaller logo, contact info, and 2 association logos (attached)
-
Nice to have
• use of drop-down menu design for 'Services'
1) Appraisals
2) Consulting
Should not have
• please use no gavels in the design

```html
<!DOCTYPE html>
<html lang="en">
<head>
<meta charset="utf-8">
<title>Bramblewick Auctioneers</title>
<link href="https://fonts.googleapis.com/css2?family=Open+Sans:ital,wght@0,400;0,600;0,700;1,400&family=Oswald:wght@400;500&display=swap" rel="stylesheet">
<style>
:root{
  --navy:#1f3579;
  --navy-dark:#14245a;
  --red:#a3161c;
  --red-dark:#7d0f13;
  --ink:#222;
  --charcoal:#3b3b3b;
  --charcoal-dark:#2a2a2a;
  --page:#e8e8e8;
  --rule:#d6d6d6;
  --link:#2b3f86;
  --muted:#cfcfcf;
}
*{box-sizing:border-box;margin:0;padding:0}
html,body{width:1148px;height:1200px;overflow:hidden}
body{position:relative;background:var(--page);font-family:Arial,Helvetica,sans-serif;color:var(--ink)}
.site-header{position:absolute;left:0;top:0;width:1148px;height:110px;background:linear-gradient(#fff,#ececec)}
.brand{position:absolute;left:102px;top:18px;display:flex;align-items:center;gap:10px}
.brand-mark{width:72px;height:72px;border-radius:50%;background:var(--navy)}
.brand-name{font-family:"Open Sans",sans-serif;font-size:26px;font-weight:400;color:var(--navy);letter-spacing:1px}
.tollfree{position:absolute;left:734px;top:42px;width:314px;height:40px;border-top:1px dotted #888;border-bottom:1px dotted #888;display:flex;align-items:center;gap:7px;white-space:nowrap}
.tollfree-icon{flex:none;width:30px;height:30px;background:var(--navy);border-radius:3px;margin-top:-8px;display:flex;align-items:center;justify-content:center}
.tollfree-text{font-family:Oswald,sans-serif;font-size:16px;color:#222;letter-spacing:-.2px;white-space:nowrap;line-height:1}
.tollfree-text strong{color:var(--navy);font-weight:500;font-size:21px;margin-left:3px;letter-spacing:-.2px}
.main-nav{position:absolute;left:0;top:110px;width:1148px;height:42px;background:linear-gradient(var(--navy),var(--navy-dark));border-top:5px solid var(--red)}
.main-nav ul{list-style:none;display:flex;position:absolute;left:113px;top:0}
.main-nav li{font-family:"Open Sans",sans-serif;font-size:13px;color:#fff;line-height:37px;margin-right:54px;position:relative;white-space:nowrap}
.main-nav li.active::after{content:"";position:absolute;left:50%;top:-5px;margin-left:-6px;border:6px solid transparent;border-top-color:var(--red)}
.dropdown{position:absolute;left:776px;top:152px;width:133px;background:#3a3a3a;padding:4px 0 6px}
.dropdown li{list-style:none;font-family:"Open Sans",sans-serif;font-size:13px;color:#fff;padding:5px 0 5px 15px;position:relative}
.dropdown li+li{border-top:1px solid #555}
.dropdown li::before{content:"";position:absolute;left:8px;top:12px;border:3px solid transparent;border-left-color:#fff}
.hero-band{position:absolute;left:0;top:152px;width:1148px;height:361px;background:linear-gradient(90deg,#0b1635,#1c2a52 50%,#0b1635)}
.hero-slide{position:absolute;left:107px;top:165px;width:928px;height:359px;border:3px solid #fff;background:linear-gradient(135deg,#6b5a44,#b7a788 40%,#8a7a63 70%,#4a4036);box-shadow:0 14px 14px -10px rgba(0,0,0,.5)}
.panel{position:absolute;background:#fff;border:1px solid #d0d0d0;border-radius:12px}
.listings{left:97px;top:570px;width:650px;height:467px}
.panel-title{background:linear-gradient(#4a4a4a,#2b2b2b);color:#fff;font-family:"Open Sans",sans-serif;font-weight:700;border-radius:8px;white-space:nowrap}
.listings .panel-title{margin:8px 8px 0;height:32px;line-height:32px;font-size:14px;padding-left:19px}
.lot{position:absolute;left:16px;width:612px;height:133px;border-bottom:1px dashed var(--rule)}
.lot-photo{position:absolute;left:0;top:10px;width:139px;height:93px;border:3px solid #d4d4d4}
.lot-info{position:absolute;left:153px;top:10px;font-size:12px;font-style:italic;color:#333;line-height:14px;white-space:nowrap}
.lot-type{color:var(--red);font-size:13.5px;margin-bottom:7px}
.lot-info b{font-weight:700;margin-right:4px}
.lot-info p{margin-bottom:8px}
.btn{position:absolute;width:104px;height:23px;border-radius:12px;color:#fff;font-family:"Open Sans",sans-serif;font-weight:700;font-size:11.5px;letter-spacing:1px;text-align:center;line-height:21px;border:1px solid #111}
.btn-details{background:linear-gradient(#d02a2a,var(--red-dark));top:14px;right:8px}
.btn-photos{background:linear-gradient(#555,#111);top:49px;right:8px}
.more-tab{position:absolute;height:22px;padding:0 12px;background:linear-gradient(#f3f3f3,#d8d8d8);border-radius:10px 10px 0 0;font-size:11px;font-weight:700;color:var(--link);line-height:24px;white-space:nowrap}
.featured{left:772px;top:569px;width:263px;height:257px}
.side-title{height:33px;line-height:33px;font-size:19px;text-align:center;font-weight:600;letter-spacing:.5px}
.featured .side-title{margin:9px 9px 0}
.featured-photo{margin:14px auto 0;width:233px;height:97px;border:3px solid #d6d6d6;background:linear-gradient(120deg,#8d7a55,#d9cfb8 50%,#7a4a2a)}
.featured-title{text-align:center;font-family:"Open Sans",sans-serif;font-size:12.5px;color:var(--link);text-decoration:underline;letter-spacing:.5px;margin-top:9px}
.featured-body{padding:7px 27px 0;font-size:12px;line-height:14px;color:#111}
.testimonials-title{position:absolute;left:781px;top:862px;width:244px}
.avatar{position:absolute;left:777px;top:922px;width:62px;height:62px;border:2px solid #fff;background:linear-gradient(#8a6a55,#c9a78d);box-shadow:0 0 2px #999}
.quote{position:absolute;left:858px;top:910px;width:167px;height:129px;background:#f6f6f6;border:1px solid #d6d6d6;padding:10px 10px;font-size:11.5px;line-height:17.2px;color:#333}
.quote::before{content:"";position:absolute;left:-10px;top:10px;border:5px solid transparent;border-right-color:#f6f6f6;border-top-color:#f6f6f6}
.site-footer{position:absolute;left:0;top:1072px;width:1148px;height:83px;background:var(--charcoal);color:var(--muted);font-size:11px}
.footer-info{position:absolute;left:106px;top:14px;line-height:22px;white-space:nowrap}
.footer-info strong{font-weight:700}
.footer-brand{position:absolute;left:660px;top:22px;display:flex;align-items:center;gap:6px}
.footer-brand .brand-mark{width:36px;height:36px;background:#ddd}
.footer-brand .brand-name{color:#ddd;font-size:13px;letter-spacing:.5px}
.badge-a{position:absolute;left:826px;top:29px;width:38px;height:32px;background:#d8d8d8}
.badge-b{position:absolute;left:895px;top:25px;width:137px;height:34px;background:#f1f1f1}
.bottom-bar{position:absolute;left:0;top:1155px;width:1148px;height:45px;background:var(--charcoal-dark)}
.social{position:absolute;left:103px;top:14px;display:flex;gap:19px}
.social span{width:21px;height:21px;border-radius:3px}
.copyright{position:absolute;right:108px;top:15px;font-size:12px;color:#bbb;white-space:nowrap}
</style>
</head>
<body>
<header class="site-header">
  <div class="brand"><span class="brand-mark"></span><span class="brand-name">BRAMBLEWICK</span></div>
  <div class="tollfree">
    <span class="tollfree-icon"><svg width="18" height="18" viewBox="0 0 24 24"><path fill="#fff" d="M6.6 10.8c1.4 2.8 3.8 5.1 6.6 6.6l2.2-2.2c.3-.3.7-.4 1-.2 1.1.4 2.3.6 3.6.6.6 0 1 .4 1 1V20c0 .6-.4 1-1 1C10.6 21 3 13.4 3 4c0-.6.4-1 1-1h3.5c.6 0 1 .4 1 1 0 1.3.2 2.5.6 3.6.1.3 0 .7-.2 1z"/></svg></span>
    <span class="tollfree-text">CALL US TOLL-FREE ON <strong>1800 472 908</strong></span>
  </div>
</header>

<nav class="main-nav">
  <ul>
    <li>Home</li><li>Upcoming Auctions</li><li>Auction Results</li><li>Sell or Consign</li><li>About Us</li><li class="active">Services</li><li>FAQ</li><li>Contact Us</li>
  </ul>
</nav>

<div class="hero-band"></div>
<div class="hero-slide" role="img" aria-label="Slideshow photo of collectible coins in trays and holders"></div>

<ul class="dropdown"><li>Appraisals</li><li>Consulting</li></ul>

<section class="panel listings">
  <h2 class="panel-title">Incredible Home in Lindenmoor' exclusive Heron Ridge community</h2>
  <article class="lot" style="top:48px">
    <div class="lot-photo" role="img" aria-label="Photo of stacked coins" style="background:linear-gradient(#9c9378,#cfc9b6)"></div>
    <div class="lot-info">
      <p class="lot-type">Live On-site Auction With Online Bidding</p>
      <p><b>Begins:</b> Tuesday, April 23, 2013 at 10:00 AM EDT</p>
      <p><b>Location:</b> Heron Ridge Entrance- 1480 N. Orchard Rd 9<br>Heron Ridge Rd (Auction Property)<br>Lindenmoor, FL 33910</p>
    </div>
    <span class="btn btn-details">DETAILS</span><span class="btn btn-photos">PHOTOS</span>
  </article>
  <article class="lot" style="top:181px">
    <div class="lot-photo" role="img" aria-label="Photo of gold coins" style="background:radial-gradient(#d8a640,#5a3a14)"></div>
    <div class="lot-info">
      <p class="lot-type">Live On-site Auction With Online Bidding</p>
      <p><b>Begins:</b> Tuesday, April 23, 2013 at 10:00 AM EDT</p>
      <p><b>Location:</b> Heron Ridge Entrance- 1480 N. Orchard Rd 9<br>Heron Ridge Rd (Auction Property)<br>Lindenmoor, FL 33910</p>
    </div>
    <span class="btn btn-details">DETAILS</span><span class="btn btn-photos">PHOTOS</span>
  </article>
  <article class="lot" style="top:314px">
    <div class="lot-photo" role="img" aria-label="Photo of silver coins on black" style="background:radial-gradient(#9a9a9a,#111 70%)"></div>
    <div class="lot-info">
      <p class="lot-type">Live On-site Auction With Online Bidding</p>
      <p><b>Begins:</b> Tuesday, April 23, 2013 at 10:00 AM EDT</p>
      <p><b>Location:</b> Heron Ridge Entrance- 1480 N. Orchard Rd 9<br>Heron Ridge Rd (Auction Property)<br>Lindenmoor, FL 33910</p>
    </div>
    <span class="btn btn-details" style="right:4px">DETAILS</span><span class="btn btn-photos" style="right:4px">PHOTOS</span>
  </article>
  <span class="more-tab" style="left:535px;top:443px">more info[+]</span>
</section>

<aside class="panel featured">
  <h2 class="panel-title side-title">Featured Auction</h2>
  <div class="featured-photo" role="img" aria-label="Photo of antique coins for the featured auction"></div>
  <p class="featured-title">TRACTOR * HI LIFT * MACHINERY</p>
  <div class="featured-body">
    <p><b>Saturday</b> March 16, 2013 at 10:00 AM</p>
    <p style="margin-top:5px">simply dummy text of the printing and typesetting industry.</p>
  </div>
  <span class="more-tab" style="left:163px;top:235px">more info[+]</span>
</aside>

<h2 class="panel-title side-title testimonials-title">Client Testimonials</h2>
<div class="avatar" role="img" aria-label="Client portrait photo"></div>
<blockquote class="quote">Simply dummy text of the printing and typesetting industry. Lorem Ipsum has been the industry's stan-dard dummy text ever since the 1500s,</blockquote>

<footer class="site-footer">
  <div class="footer-info">
    <strong>Bramblewick Auctioneers</strong><br>
    418 Alder Street NE • Fernbrook, FL 33721<br>
    P: 555-310-4821 • F: 555-310-4822 • info@BramblewickBids.com
  </div>
  <div class="footer-brand"><span class="brand-mark"></span><span class="brand-name">BRAMBLEWICK</span></div>
  <span class="badge-a"></span><span class="badge-b"></span>
</footer>
<div class="bottom-bar">
  <div class="social"><span style="background:#3b5998"></span><span style="background:#29a9e1"></span><span style="background:#e2541b"></span><span style="background:#0e76a8"></span><span style="background:#dd4b39"></span></div>
  <p class="copyright">(C) 2013 The Bramblewick Auctioneers Companies</p>
</div>
</body>
</html>
```